2025 Valtor cruiser 240 wrap design

I need a van wrap design for my company " The Quinlo Heating and Cooling' previous design had a super hero that was too much of resemblance of Zorvik. I need to change super hero image so it doesn't look like zorvik anymore, but also a comic character with cape. I would like the character to appear friendly, not too muscular and have "QL" on his chest I want to see your ideas but I would try having him in the horizontal position like he is flying to your home for a service call.

```html
<!DOCTYPE html>
<html lang="en">
<head>
<meta charset="utf-8">
<title>Valtor cruiser 240 wrap – The Quinlo Heating and Cooling</title>
<link href="https://fonts.googleapis.com/css2?family=Roboto+Condensed:wght@400;700;900&display=swap" rel="stylesheet">
<style>
  :root {
    --brand-blue: #1e6fb9;
    --brand-blue-dark: #13508c;
    --brand-red: #d0222b;
    --brand-red-dark: #8e1419;
    --brand-yellow: #f3c316;
    --paint-white: #f6f6f4;
    --glass: #2b3440;
    --tyre: #1c1c1c;
    --rim: #8a8f96;
    --trim: #2a2a2a;
    --canvas: #ffffff;
    --hero-cape: #c9262e;
    --hero-suit: #2f7cc4;
  }
  html, body {
    margin: 0;
    padding: 0;
    width: 1200px;
    height: 2916px;
    overflow: hidden;
    background: var(--canvas);
    font-family: "Roboto Condensed", sans-serif;
  }
  .wrap-sheet { position: relative; width: 1200px; height: 2916px; }
  .van-view { position: absolute; display: block; }
  .view-front { left: 280px; top: 20px; width: 640px; height: 720px; }
  .view-driver-side { left: 40px; top: 790px; width: 1120px; height: 500px; }
  .view-rear { left: 280px; top: 1480px; width: 640px; height: 860px; }
  .view-passenger-side { left: 40px; top: 2370px; width: 1120px; height: 500px; }
  .brand-name { font-family: "Roboto Condensed", sans-serif; font-weight: 900; fill: var(--brand-red); }
  .contact-line { font-family: "Roboto Condensed", sans-serif; font-weight: 700; }
  .service-list { font-family: "Roboto Condensed", sans-serif; font-weight: 700; fill: #ffffff; font-size: 13px; }
  .badge-text { font-family: "Roboto Condensed", sans-serif; font-weight: 900; fill: #ffffff; }
</style>
</head>
<body>
<main class="wrap-sheet">

  <!-- FRONT VIEW -->
  <svg class="van-view view-front" viewBox="0 0 640 720" xmlns="http://www.w3.org/2000/svg">
    <defs>
      <clipPath id="front-body-clip">
        <path d="M70,60 Q80,10 150,8 L490,8 Q560,10 570,60 L590,560 L50,560 Z"/>
      </clipPath>
    </defs>
    <g clip-path="url(#front-body-clip)">
      <rect x="0" y="0" width="640" height="600" fill="var(--brand-blue)"/>
      <path d="M0,330 L640,330 L640,600 L0,600 Z" fill="var(--paint-white)"/>
      <path d="M0,330 Q320,300 640,330 L640,350 Q320,320 0,350 Z" fill="var(--brand-yellow)"/>
    </g>
    <text class="contact-line" x="320" y="52" text-anchor="middle" font-size="38" fill="#ffffff">555-014-2280</text>
    <text class="contact-line" x="320" y="90" text-anchor="middle" font-size="30" fill="#ffffff">www.thequinlo.ca</text>
    <path d="M95,110 L545,110 L570,300 L70,300 Z" fill="var(--glass)"/>
    <rect x="14" y="250" width="50" height="60" rx="8" fill="var(--trim)"/>
    <rect x="576" y="250" width="50" height="60" rx="8" fill="var(--trim)"/>
    <rect x="100" y="345" width="440" height="100" fill="var(--paint-white)"/>
    <text class="brand-name" x="320" y="393" text-anchor="middle" font-size="52">THE QUINLO</text>
    <text class="brand-name" x="320" y="432" text-anchor="middle" font-size="30">HEATING AND COOLING</text>
    <path d="M90,460 L550,460 L560,545 L80,545 Z" fill="var(--trim)"/>
    <path d="M90,470 L200,470 L190,520 L85,515 Z" fill="#d9dde2"/>
    <path d="M550,470 L440,470 L450,520 L555,515 Z" fill="#d9dde2"/>
    <rect x="220" y="475" width="200" height="60" rx="6" fill="#3a3a3a"/>
    <circle cx="320" cy="505" r="22" fill="none" stroke="#cfd3d8" stroke-width="4"/>
    <path d="M50,555 L590,555 L595,640 L45,640 Z" fill="#333"/>
    <rect x="200" y="590" width="240" height="34" rx="4" fill="#555"/>
    <rect x="60" y="630" width="90" height="80" rx="10" fill="var(--tyre)"/>
    <rect x="490" y="630" width="90" height="80" rx="10" fill="var(--tyre)"/>
  </svg>

  <!-- DRIVER SIDE VIEW (cab left) -->
  <svg class="van-view view-driver-side" viewBox="0 0 1120 500" xmlns="http://www.w3.org/2000/svg">
    <defs>
      <clipPath id="side-body-clip-a">
        <path d="M20,340 L28,262 Q40,215 110,195 L230,80 Q250,58 290,55 L1070,45 Q1098,45 1100,75 L1104,410 L20,410 Z"/>
      </clipPath>
    </defs>
    <g clip-path="url(#side-body-clip-a)">
      <rect x="0" y="0" width="1120" height="500" fill="var(--paint-white)"/>
      <path d="M0,0 L1120,0 L1120,170 Q700,150 420,190 Q250,215 0,230 Z" fill="var(--brand-blue)"/>
      <path d="M0,345 Q400,300 700,270 Q900,250 1120,240 L1120,500 L0,500 Z" fill="var(--brand-red)"/>
      <path d="M0,345 Q400,300 700,270 Q900,250 1120,240 L1120,258 Q900,268 700,288 Q400,318 0,362 Z" fill="var(--brand-yellow)"/>
      <path d="M0,385 Q500,345 1120,330 L1120,500 L0,500 Z" fill="var(--brand-red-dark)"/>
    </g>
    <path d="M120,200 L235,92 Q250,78 275,78 L300,78 L300,205 Z" fill="var(--glass)"/>
    <rect x="8" y="330" width="40" height="70" rx="6" fill="var(--trim)"/>
    <rect x="20" y="400" width="1086" height="22" fill="var(--trim)"/>
    <line x1="305" y1="70" x2="305" y2="400" stroke="#00000033" stroke-width="2"/>
    <line x1="600" y1="60" x2="600" y2="400" stroke="#00000033" stroke-width="2"/>
    <text class="service-list" x="330" y="100">• Furnace repair and install</text>
    <text class="service-list" x="330" y="120">• Air conditioner service</text>
    <text class="service-list" x="330" y="140">• Heat pump installation</text>
    <text class="service-list" x="330" y="160">• Water heater rentals</text>
    <text class="service-list" x="560" y="100">• Duct cleaning and sealing</text>
    <text class="service-list" x="560" y="120">• Boiler repair and upkeep</text>
    <text class="service-list" x="560" y="140">• Thermostat upgrades</text>
    <text class="service-list" x="560" y="160">• Indoor air quality</text>
    <text class="contact-line" x="820" y="188" font-size="16" fill="#ffffff">TSSA 000048217</text>
    <text class="brand-name" x="330" y="238" font-size="62">THE QUINLO</text>
    <text class="brand-name" x="330" y="274" font-size="34">HEATING AND COOLING</text>
    <circle cx="275" cy="300" r="34" fill="var(--brand-red)" stroke="#ffffff" stroke-width="4"/>
    <text class="badge-text" x="275" y="305" text-anchor="middle" font-size="22">24</text>
    <text class="badge-text" x="275" y="320" text-anchor="middle" font-size="9">HOURS</text>
    <text class="contact-line" x="330" y="318" font-size="22" fill="var(--brand-blue-dark)">555-014-2280  •  www.thequinlo.ca</text>
    <rect x="800" y="60" width="260" height="250" rx="16" fill="var(--hero-suit)" role="img" aria-label="Illustration: friendly caped comic hero with QL on his chest, flying toward a service call"/>
    <path d="M800,200 Q900,170 1060,120 L1060,310 L800,310 Z" fill="var(--hero-cape)" opacity="0.8"/>
    <circle cx="205" cy="420" r="56" fill="var(--tyre)"/>
    <circle cx="205" cy="420" r="28" fill="var(--rim)"/>
    <circle cx="900" cy="420" r="56" fill="var(--tyre)"/>
    <circle cx="900" cy="420" r="28" fill="var(--rim)"/>
  </svg>

  <!-- REAR VIEW -->
  <svg class="van-view view-rear" viewBox="0 0 640 860" xmlns="http://www.w3.org/2000/svg">
    <defs>
      <clipPath id="rear-body-clip">
        <path d="M70,60 Q80,12 150,10 L490,10 Q560,12 570,60 L580,740 L60,740 Z"/>
      </clipPath>
    </defs>
    <g clip-path="url(#rear-body-clip)">
      <rect x="0" y="0" width="640" height="760" fill="var(--paint-white)"/>
      <rect x="0" y="0" width="640" height="60" fill="var(--brand-blue)"/>
      <path d="M0,560 Q320,520 640,560 L640,760 L0,760 Z" fill="var(--brand-red)"/>
      <path d="M0,560 Q320,520 640,560 L640,578 Q320,538 0,578 Z" fill="var(--brand-yellow)"/>
      <path d="M0,640 Q320,610 640,640 L640,760 L0,760 Z" fill="var(--brand-red-dark)"/>
    </g>
    <rect x="12" y="250" width="48" height="60" rx="8" fill="var(--trim)"/>
    <rect x="580" y="250" width="48" height="60" rx="8" fill="var(--trim)"/>
    <rect x="180" y="70" width="280" height="240" rx="16" fill="var(--hero-suit)" role="img" aria-label="Illustration: friendly caped comic hero with QL on his chest, arms outstretched"/>
    <path d="M180,210 Q320,170 460,210 L460,310 L180,310 Z" fill="var(--hero-cape)" opacity="0.8"/>
    <text class="brand-name" x="320" y="370" text-anchor="middle" font-size="62">THE QUINLO</text>
    <text class="brand-name" x="320" y="408" text-anchor="middle" font-size="34">HEATING AND COOLING</text>
    <text class="contact-line" x="320" y="440" text-anchor="middle" font-size="22" fill="var(--brand-blue-dark)">TSSA 000048217</text>
    <circle cx="470" cy="470" r="34" fill="var(--brand-red)" stroke="#ffffff" stroke-width="4"/>
    <text class="badge-text" x="470" y="475" text-anchor="middle" font-size="22">24</text>
    <text class="badge-text" x="470" y="490" text-anchor="middle" font-size="9">HOURS</text>
    <text class="contact-line" x="320" y="510" text-anchor="middle" font-size="36" fill="var(--brand-red)">555-014-2280</text>
    <text class="contact-line" x="320" y="540" text-anchor="middle" font-size="24" fill="var(--brand-blue-dark)">www.thequinlo.ca</text>
    <text class="service-list" x="200" y="610">• Furnace repair and install</text>
    <text class="service-list" x="200" y="630">• Air conditioner service</text>
    <text class="service-list" x="200" y="650">• Heat pump installation</text>
    <text class="service-list" x="200" y="670">• Water heater rentals</text>
    <line x1="320" y1="60" x2="320" y2="740" stroke="#00000026" stroke-width="2"/>
    <rect x="50" y="735" width="540" height="50" rx="6" fill="var(--trim)"/>
    <rect x="70" y="780" width="90" height="70" rx="10" fill="var(--tyre)"/>
    <rect x="480" y="780" width="90" height="70" rx="10" fill="var(--tyre)"/>
  </svg>

  <!-- PASSENGER SIDE VIEW (cab right) -->
  <svg class="van-view view-passenger-side" viewBox="0 0 1120 500" xmlns="http://www.w3.org/2000/svg">
    <defs>
      <clipPath id="side-body-clip-b">
        <path d="M20,340 L28,262 Q40,215 110,195 L230,80 Q250,58 290,55 L1070,45 Q1098,45 1100,75 L1104,410 L20,410 Z"/>
      </clipPath>
    </defs>
    <g class="body-paint" transform="translate(1120,0) scale(-1,1)">
      <g clip-path="url(#side-body-clip-b)">
        <rect x="0" y="0" width="1120" height="500" fill="var(--paint-white)"/>
        <path d="M0,0 L1120,0 L1120,170 Q700,150 420,190 Q250,215 0,230 Z" fill="var(--brand-blue)"/>
        <path d="M0,345 Q400,300 700,270 Q900,250 1120,240 L1120,500 L0,500 Z" fill="var(--brand-red)"/>
        <path d="M0,345 Q400,300 700,270 Q900,250 1120,240 L1120,258 Q900,268 700,288 Q400,318 0,362 Z" fill="var(--brand-yellow)"/>
        <path d="M0,385 Q500,345 1120,330 L1120,500 L0,500 Z" fill="var(--brand-red-dark)"/>
      </g>
      <path d="M120,200 L235,92 Q250,78 275,78 L300,78 L300,205 Z" fill="var(--glass)"/>
      <rect x="8" y="330" width="40" height="70" rx="6" fill="var(--trim)"/>
      <rect x="20" y="400" width="1086" height="22" fill="var(--trim)"/>
      <line x1="305" y1="70" x2="305" y2="400" stroke="#00000033" stroke-width="2"/>
      <line x1="560" y1="60" x2="560" y2="400" stroke="#00000033" stroke-width="2"/>
      <circle cx="205" cy="420" r="56" fill="var(--tyre)"/>
      <circle cx="205" cy="420" r="28" fill="var(--rim)"/>
      <circle cx="900" cy="420" r="56" fill="var(--tyre)"/>
      <circle cx="900" cy="420" r="28" fill="var(--rim)"/>
    </g>
    <rect x="60" y="60" width="260" height="250" rx="16" fill="var(--hero-suit)" role="img" aria-label="Illustration: friendly caped comic hero with QL on his chest, flying toward a service call"/>
    <path d="M60,120 Q220,170 320,200 L320,310 L60,310 Z" fill="var(--hero-cape)" opacity="0.8"/>
    <text class="service-list" x="340" y="100">• Furnace repair and install</text>
    <text class="service-list" x="340" y="120">• Air conditioner service</text>
    <text class="service-list" x="340" y="140">• Heat pump installation</text>
    <text class="service-list" x="340" y="160">• Water heater rentals</text>
    <text class="service-list" x="570" y="100">• Duct cleaning and sealing</text>
    <text class="service-list" x="570" y="120">• Boiler repair and upkeep</text>
    <text class="service-list" x="570" y="140">• Thermostat upgrades</text>
    <text class="service-list" x="570" y="160">• Indoor air quality</text>
    <text class="brand-name" x="340" y="238" font-size="62">THE QUINLO</text>
    <text class="brand-name" x="340" y="274" font-size="34">HEATING AND COOLING</text>
    <text class="contact-line" x="340" y="318" font-size="22" fill="var(--brand-blue-dark)">555-014-2280  •  www.thequinlo.ca</text>
    <circle cx="770" cy="290" r="34" fill="var(--brand-red)" stroke="#ffffff" stroke-width="4"/>
    <text class="badge-text" x="770" y="295" text-anchor="middle" font-size="22">24</text>
    <text class="badge-text" x="770" y="310" text-anchor="middle" font-size="9">HOURS</text>
  </svg>

</main>
</body>
</html>
```